Business Card Design for Retail Product Line

We need a two-sided, full-color business card for a new oral care product line. The feel of the card should invoke emotions of happiness and health. It should be bright, cheerful and modern in appearance. The card should be mostly matte finish, but with elements of spot-gloss and/or raised/embossed features (print, logo, tag lines, etc.).

Target Market(s)

People who are into whole-body health, eat well and understand the importance of nutrition.

Industry/Entity Type

Health And Wellness

Contact Information for Business Card

The logo, color scheme and tag-lines have all been developed and artwork is attached. Card is to be standard-sized and should use a mix of clean, sans-serif fonts; the main font (DIN) is attached as well. The card will be used for 3 individuals and should include placeholders for:
1. Name
2. Title (for example, "CEO")
3. Business address
4. Phone number
5. Website
6. Email address

Font styles to use
Sans Serif
Other font styles liked:
• DIN font

Colors
faa54b
000000
5c5c5c
a2ce44

Requirements
Must have
• 2 sides
• Full color orange on one side
• Image of DNA leaves
• Tag line "Glow from the Root Upward", on single side with orange background
• Company Logo (Plome) on same side as text (name, phone, address, etc.)
• Name, Title, Business Address, Phone Number, Website, Email address
• UPDATE: "Brisk Marrow", not "Brisk M Arrow"
Should not have
• Calligraphy
• Dark colors
• UPDATE!! Do not include "Turmeric infused toothpaste" on the business card
• UPDATE #2!! Do not include "Brisk Marrow" on the business card

```html
<!DOCTYPE html>
<html lang="en">
<head>
<meta charset="utf-8">
<title>Plome Business Card</title>
<link rel="stylesheet" href="https://fonts.googleapis.com/css2?family=Montserrat:wght@400;500;600;700&display=swap">
<style>
  :root {
    --bg: #ececec;
    --orange-light: #f5cc3c;
    --orange: #f0b233;
    --orange-deep: #e8983a;
    --band: #f0ad12;
    --green: #2a8a3e;
    --leaf: #a2ce44;
    --grey: #5c5c5c;
    --ink: #3a3a3a;
    --paper: #ffffff;
    --emboss: #f1f1f1;
  }
  * { box-sizing: border-box; margin: 0; padding: 0; }
  html, body { width: 1200px; height: 900px; overflow: hidden; }
  body {
    background: var(--bg);
    font-family: "Montserrat", sans-serif;
    position: relative;
  }
  .card {
    position: absolute;
    width: 560px;
    height: 320px;
    border-radius: 18px;
    overflow: hidden;
    box-shadow: 0 10px 28px rgba(0,0,0,0.18);
  }

  /* Front */
  .card-front {
    left: 90px; top: 90px;
    background: linear-gradient(200deg, var(--orange-light) 0%, var(--orange) 45%, var(--orange-deep) 100%);
  }
  .front-brand {
    position: absolute;
    left: 0; right: 0; top: 108px;
    text-align: center;
    color: var(--paper);
    font-weight: 700;
    font-size: 72px;
    letter-spacing: 1px;
  }
  .front-web {
    position: absolute;
    left: 0; right: 0; top: 246px;
    text-align: center;
    color: var(--paper);
    font-size: 15px;
    font-weight: 500;
    letter-spacing: 1px;
  }
  .dna-art {
    position: absolute;
    right: 34px; top: 40px;
    width: 70px; height: 100px;
    border-radius: 10px;
    background: linear-gradient(180deg, var(--leaf) 0%, #7fb33a 40%, #c9c9c9 100%);
  }

  /* Back */
  .card-back {
    left: 550px; top: 480px;
    background: var(--paper);
  }
  .back-brand {
    position: absolute;
    left: 40px; top: 96px;
    width: 220px;
    text-align: center;
    color: var(--emboss);
    font-weight: 700;
    font-size: 64px;
    text-shadow: none;
  }
  .divider {
    position: absolute;
    left: 282px; top: 48px;
    width: 1px; height: 150px;
    background: #bdbdbd;
  }
  .contact {
    position: absolute;
    left: 305px; top: 46px;
    color: var(--ink);
  }
  .contact-name {
    color: var(--orange);
    font-weight: 700;
    font-size: 22px;
    line-height: 1.1;
  }
  .contact-title {
    font-size: 13px;
    color: var(--grey);
    margin-bottom: 8px;
  }
  .contact-line {
    display: flex;
    align-items: center;
    gap: 7px;
    font-size: 13px;
    line-height: 20px;
  }
  .contact-line svg { width: 10px; height: 10px; flex: none; }
  .contact-line .web-accent { color: var(--green); font-weight: 700; }
  .address {
    margin-top: 6px;
    margin-left: 17px;
    font-size: 13px;
    line-height: 18px;
  }
  .band {
    position: absolute;
    left: 0; right: 0; top: 240px;
    height: 30px;
    background: var(--band);
  }
  .tagline {
    position: absolute;
    left: 210px; top: 234px;
    padding: 0 18px;
    height: 42px;
    line-height: 38px;
    border: 2px solid var(--paper);
    border-radius: 7px;
    background: var(--green);
    color: var(--paper);
    font-weight: 700;
    font-size: 14px;
    text-transform: uppercase;
    letter-spacing: 0.3px;
  }
</style>
</head>
<body>
  <section class="card card-front">
    <div class="front-brand">plome</div>
    <div class="front-web">www.plome.com</div>
    <div class="dna-art" role="img" aria-label="DNA strand with green leaves illustration"></div>
  </section>

  <section class="card card-back">
    <div class="back-brand">plome</div>
    <div class="divider"></div>
    <div class="contact">
      <div class="contact-name">Marlo Trent</div>
      <div class="contact-title">Director</div>
      <div class="contact-line">
        <svg viewBox="0 0 10 10"><path d="M2 1 L4 1 L4.6 3 L3.4 3.8 Q4.6 6 6.2 6.6 L7 5.4 L9 6 L9 8 Q5 9 1 3 Z" fill="var(--orange)"/></svg>
        <span>+330 5550-0193</span>
      </div>
      <div class="contact-line">
        <svg viewBox="0 0 10 10"><rect x="0.8" y="2" width="8.4" height="6" fill="none" stroke="var(--orange)" stroke-width="1.2"/><path d="M1 2.4 L5 5.4 L9 2.4" fill="none" stroke="var(--orange)" stroke-width="1.2"/></svg>
        <span>info@plome.com</span>
      </div>
      <div class="contact-line">
        <svg viewBox="0 0 10 10"><circle cx="5" cy="5" r="4.2" fill="none" stroke="var(--orange)" stroke-width="1.2"/><path d="M1 5 H9 M5 1 Q2.5 5 5 9 Q7.5 5 5 1" fill="none" stroke="var(--orange)" stroke-width="0.9"/></svg>
        <span>www.<span class="web-accent">plome</span>.com</span>
      </div>
      <div class="address">2218 Larkspur Ave.<br>Fairmont CA 90310</div>
    </div>
    <div class="band"></div>
    <div class="tagline">Glow from the Root Upward</div>
  </section>
</body>
</html>
```